Annual review for The Heron Collective

The Heron Collective is a small public relations agency in London specialising in corporate and public affairs. Most of our work is international and we have a strong connection to South Africa. We would like to prepare a short annual review for 2016. The review will serve as both a review of our activities in 2016, and as a credentials document. Content then will include:
1. An introduction to the business
2. Who we are
3. Projects and clients undertaken in 2016
4. News and views
We imagine it will be used mostly as a pdf but would like it to be suitable for print. We envisage it to be about 8 pages long. The design look and feel should convey a business, while small, of stature. We shall include some of our client logos but we would welcome the use of some photography / imagery to have visual impact (although we don't have very much of our own!). The corporate look and feel is white, grey and black.

Industry/Entity Type

Public Relation

Font styles to use
Sans Serif

Requirements
Must have
• My project must convey a business with flair and gravitas, that punches above its weight.
Nice to have
• Thoughtful use of imagery.

```html
<!DOCTYPE html>
<html lang="en">
<head>
<meta charset="utf-8">
<title>The Heron Collective – Annual Review</title>
<link rel="stylesheet" href="https://fonts.googleapis.com/css2?family=Fira+Sans:ital,wght@0,400;0,600;0,700;1,700&family=Oswald:wght@300&display=swap">
<style>
  :root {
    --backdrop: #e7e4df;
    --paper: #ffffff;
    --steel: #a3bbc6;
    --steel-light: #cddbe1;
    --steel-deep: #7f9ca9;
    --ink: #1f2326;
    --body: #2e3236;
    --olive: #4d5b3d;
    --rule: #9aa3a8;
    --tab: #4a4d50;
    --brand: #6a8592;
    --photo-dark: #3b4247;
    --photo-mid: #7d868b;
    --photo-light: #b9c0c3;
  }
  * { box-sizing: border-box; margin: 0; padding: 0; }
  html, body { width: 1200px; height: 2300px; overflow: hidden; }
  body { background: var(--backdrop); position: relative; font-family: "Fira Sans", Arial, sans-serif; color: var(--body); }

  .page { position: absolute; width: 540px; height: 420px; overflow: hidden; box-shadow: 0 3px 10px rgba(0,0,0,.22); }
  .col-left { left: 38px; }
  .col-right { left: 622px; }
  .row-1 { top: 22px; } .row-2 { top: 468px; } .row-3 { top: 922px; } .row-4 { top: 1374px; } .row-5 { top: 1826px; }

  .page--steel { background: linear-gradient(100deg, var(--steel) 0%, var(--steel-light) 100%); }
  .page--paper { background: var(--paper); }

  .photo { position: absolute; }
  .brand { display: flex; align-items: center; gap: 7px; color: var(--brand); font-size: 13px; font-weight: 400; white-space: nowrap; }
  .brand-dot { width: 13px; height: 13px; border-radius: 50%; border: 1.5px solid currentColor; flex: none; }

  /* cover */
  .cover { border: 8px solid #eef2f3; }
  .cover .brand { position: absolute; left: 24px; top: 46px; color: var(--ink); font-size: 14px; }
  .cover-photo { right: 2px; top: 3px; width: 290px; height: 396px; clip-path: polygon(0 0, 100% 0, 100% 100%, 70% 100%); background: linear-gradient(160deg, var(--photo-dark) 0%, var(--photo-mid) 45%, var(--photo-light) 62%, var(--photo-dark) 100%); }
  .cover-title { position: absolute; left: 22px; top: 104px; font-family: "Oswald", "Arial Narrow", sans-serif; font-weight: 300; font-size: 58px; line-height: 60px; color: var(--ink); letter-spacing: 1px; }
  .cover-lede { position: absolute; left: 24px; top: 292px; width: 215px; font-size: 8.5px; line-height: 11px; color: var(--ink); }

  /* quote spreads */
  .pull-quote { position: absolute; font-weight: 700; font-style: italic; font-size: 10px; line-height: 13px; color: var(--ink); }

  /* text pages */
  .tab { position: absolute; right: 34px; top: 0; width: 26px; height: 40px; background: var(--tab); display: flex; align-items: flex-end; justify-content: center; padding-bottom: 7px; }
  .tab span { width: 11px; height: 11px; border: 1.5px solid #fff; border-radius: 50%; }
  .section-title { position: absolute; left: 40px; top: 40px; font-size: 17px; font-weight: 700; color: var(--olive); }
  .section-rule { position: absolute; left: 40px; right: 40px; top: 68px; height: 1px; background: var(--rule); }
  .copy { position: absolute; left: 40px; right: 40px; top: 80px; font-size: 8.2px; line-height: 10.6px; text-align: justify; color: var(--body); }
  .copy p + p { margin-top: 7px; }
  .page-foot { position: absolute; right: 40px; bottom: 16px; }
  .page-foot .brand { font-size: 12px; }

  /* feature page */
  .feature-band { position: absolute; left: 0; right: 0; top: 0; height: 40px; background: linear-gradient(90deg, var(--steel-light), var(--steel)); }
  .feature-band .brand { position: absolute; left: 130px; top: 12px; color: var(--brand); font-size: 14px; }
  .feature-copy { position: absolute; left: 82px; top: 52px; width: 262px; font-size: 8.4px; line-height: 11px; color: var(--body); }
  .feature-copy p + p { margin-top: 8px; }
  .feature-quote { position: absolute; left: 390px; top: 118px; width: 138px; font-size: 8.4px; line-height: 11px; font-style: italic; color: var(--brand); }

  /* back cover */
  .back-panel { position: absolute; inset: 14px; background: linear-gradient(100deg, var(--steel-deep) 0%, var(--steel-light) 100%); }
  .back-panel .brand { position: absolute; left: 30px; top: 230px; color: #4e6470; font-size: 15px; }
  .contact { position: absolute; top: 290px; font-size: 8px; line-height: 11px; color: var(--ink); }
  .contact--london { left: 30px; }
  .contact--cape { left: 270px; }
  .contact-email { position: absolute; left: 30px; top: 346px; font-size: 8px; color: var(--ink); }
</style>
</head>
<body>

<!-- Cover -->
<section class="page page--steel cover col-left row-1">
  <div class="brand"><span class="brand-dot"></span>The Heron Collective</div>
  <h1 class="cover-title">ANNUAL<br>REPORT 2017</h1>
  <p class="cover-lede">A year of counsel, campaigns and conversations across London and South Africa. This review sets out who we are, the clients we served and the projects that shaped our work in 2016.</p>
  <div class="photo cover-photo" role="img" aria-label="Black and white photograph of a rugged coastline with waves breaking on a rocky headland"></div>
</section>

<!-- Quote spread 1 -->
<section class="page page--steel col-right row-1">
  <div class="photo" role="img" aria-label="Black and white photograph of a man standing on a tall stool in the sea, looking through binoculars" style="left:73px;top:121px;width:241px;height:221px;background:linear-gradient(180deg,#d8dcde 0%,#aeb4b7 60%,#5d6468 100%);"></div>
  <p class="pull-quote" style="left:361px;top:121px;width:172px;">"We look further than the headline. Good counsel begins with seeing the whole horizon, then choosing the one message that carries across it. Every client deserves that view."</p>
</section>

<!-- Introduction -->
<section class="page page--paper col-left row-2">
  <div class="tab"><span></span></div>
  <h2 class="section-title">Introduction</h2>
  <div class="section-rule"></div>
  <div class="copy">
    <p>The Heron Collective is a small public relations agency based in London, specialising in corporate and public affairs. Our work crosses borders: most of what we do is international, and for many years we have kept a close working bond with partners, clients and communities in South Africa. We advise boards, founders and public bodies on how to explain themselves clearly to the people who matter most to them.</p>
    <p>In 2016 we grew our client list, opened new conversations with policy makers and delivered campaigns in four countries. We stayed deliberately small, because small teams move quickly, listen closely and take personal ownership of results. Each client works directly with a senior partner from the first meeting to the final report, and that continuity is what clients tell us they value most.</p>
    <p>This review looks back on that year. It is both a record of our activity and an introduction to how we work, for clients who already know us and for those who may wish to. We describe our team, the projects we undertook, and the ideas that shaped our thinking across a busy and often surprising twelve months.</p>
    <p>We believe reputation is built slowly and lost quickly. Our role is to help organisations earn trust through plain words, steady conduct and well judged timing. Whether the task is a market entry, a difficult announcement or a long campaign for policy change, we bring the same calm approach and the same care for detail.</p>
    <p>We are grateful to every client and partner who placed their confidence in us during 2016, and we look forward to the year ahead with energy and ambition.</p>
  </div>
  <div class="page-foot"><div class="brand"><span class="brand-dot"></span>The Heron Collective</div></div>
</section>

<!-- Quote spread 2 -->
<section class="page page--steel col-right row-2">
  <p class="pull-quote" style="left:169px;top:52px;width:364px;">"Reputation is the quiet work of many seasons. We plant carefully, tend patiently and gather only when the moment is right, so that every message lands with weight and purpose."</p>
  <div class="photo" role="img" aria-label="Black and white photograph of people working in a rice field under a misty sky" style="left:160px;top:163px;width:269px;height:154px;background:linear-gradient(180deg,#e1e4e5 0%,#a9afb2 45%,#5f676b 100%);"></div>
</section>

<!-- Who We Are -->
<section class="page page--paper col-left row-3">
  <div class="tab"><span></span></div>
  <h2 class="section-title">Who We Are</h2>
  <div class="section-rule"></div>
  <div class="copy">
    <p>We are a team of six senior consultants with backgrounds in journalism, government, diplomacy and corporate communications. Between us we have advised listed companies, development agencies, charities and ministries on three continents. We speak the languages of the boardroom and the newsroom, and we know when each is needed.</p>
    <p>Our founding partners set up the business with a simple idea: that clients should always be served by the people they meet at the pitch. We have kept to that promise. There are no junior handovers, no layers of account management and no wasted words in our reports.</p>
    <p>Our South African connection runs deep. Several of our team have lived and worked in Johannesburg and Cape Town, and we maintain trusted relationships with media, investors and civil society there. That knowledge allows us to guide clients moving between London and southern Africa with confidence and sensitivity.</p>
    <p>We work in corporate reputation, public affairs, stakeholder engagement, crisis preparation and executive positioning. We write strategies, draft speeches, train spokespeople and manage the long relationships that turn one good story into lasting standing.</p>
    <p>Above all we are independent. We choose our clients carefully and we give honest advice, even when it is not the easiest advice to hear.</p>
  </div>
  <div class="page-foot"><div class="brand"><span class="brand-dot"></span>The Heron Collective</div></div>
</section>

<!-- Quote spread 3 -->
<section class="page page--steel col-right row-3">
  <p class="pull-quote" style="left:67px;top:52px;width:323px;">"Carrying a message well is a matter of balance. We weigh every word, steady every step and keep the load even, so the story arrives whole at its destination."</p>
  <div class="photo" role="img" aria-label="Black and white photograph of a farmer carrying baskets on a shoulder pole through a misty field" style="left:63px;top:138px;width:337px;height:225px;background:linear-gradient(170deg,#c9ced0 0%,#8e969a 50%,#4a5256 100%);"></div>
</section>

<!-- Projects and Clients -->
<section class="page page--paper col-left row-4">
  <div class="tab"><span></span></div>
  <h2 class="section-title">Projects and Clients Undertaken in 2016</h2>
  <div class="section-rule"></div>
  <div class="copy">
    <p>The year brought a wide range of assignments. We supported an energy company through a major investment announcement in the Western Cape, coordinating media briefings in London and Johannesburg on the same morning. The launch earned coverage in every national title we targeted and opened doors with regional officials.</p>
    <p>For a development foundation we designed a two year public affairs programme to build support for rural education funding. The work included a parliamentary reception, a published research paper and a series of roundtables that brought together teachers, donors and civil servants.</p>
    <p>We advised a listed mining group on stakeholder relations during a period of community concern, helping the board to listen first and then to speak with clarity. We also trained its senior leaders for broadcast interviews and public hearings.</p>
    <p>Other clients included a boutique investment house entering the London market, a wine estate seeking international distribution, a medical charity marking its twentieth anniversary and a technology start up preparing for its first funding round.</p>
    <p>Across all of these projects our aim was the same: to help clients be understood, trusted and remembered by the audiences that shape their future. We are proud of the results and of the relationships that grew from them, many of which continue into the new year.</p>
  </div>
  <div class="page-foot"><div class="brand"><span class="brand-dot"></span>The Heron Collective</div></div>
</section>

<!-- Feature page -->
<section class="page page--paper col-right row-4">
  <div class="feature-band"><div class="brand"><span class="brand-dot"></span>The Heron Collective</div></div>
  <div class="feature-copy">
    <p>Our community work matters to us. During 2016 we gave time to a literacy project near Stellenbosch, helping its volunteers tell their story to new donors and partners in Europe. Small efforts, carefully made, can change the way a project is seen.</p>
    <p>We also mentored young communicators from both countries, sharing practical skills in writing, media handling and campaign planning. Several have since joined newsrooms and agencies of their own, and we remain in touch with each of them.</p>
  </div>
  <p class="feature-quote">"In every place we work, we try to leave something lasting: a skill, a voice, a story told well."</p>
  <div class="photo" role="img" aria-label="Black and white photograph of a smiling child resting against a wooden post" style="left:0;top:244px;width:540px;height:176px;background:linear-gradient(90deg,#6d757a 0%,#9aa1a5 40%,#2f3538 75%,#1c2023 100%);"></div>
</section>

<!-- News and Views -->
<section class="page page--paper col-left row-5">
  <div class="tab"><span></span></div>
  <h2 class="section-title">News and Views</h2>
  <div class="section-rule"></div>
  <div class="copy">
    <p>It was a year of change in politics and in media. Voters surprised forecasters on both sides of the Atlantic, and trust in institutions was tested again and again. For communicators the lesson was clear: audiences reward honesty and punish spin, and they notice the difference faster than ever.</p>
    <p>We welcomed two new consultants to the team, one with a long career in financial journalism and one from the diplomatic service. Their experience has already strengthened our work on investor relations and international public affairs.</p>
    <p>Our partners spoke at conferences in London, Cape Town and Nairobi on the future of corporate reputation in Africa. We argued that companies investing on the continent must explain their purpose locally before they explain it to shareholders abroad.</p>
    <p>We also published short essays on crisis readiness, on the role of chief executives as public voices, and on the quiet power of listening. Each drew thoughtful responses from clients and peers, and several led to new conversations and new work.</p>
    <p>Looking ahead, we expect greater scrutiny, faster news cycles and more demanding stakeholders. We see these as reasons for optimism. They favour organisations that are clear about who they are, and advisers who help them say it well.</p>
  </div>
  <div class="page-foot"><div class="brand"><span class="brand-dot"></span>The Heron Collective</div></div>
</section>

<!-- Back cover -->
<section class="page page--paper col-right row-5">
  <div class="back-panel">
    <div class="brand"><span class="brand-dot"></span>The Heron Collective</div>
    <p class="contact contact--london">The Heron Collective<br>14 Alder Row<br>London EC2A 4LP</p>
    <p class="contact contact--cape">The Heron Collective<br>9 Kloof Terrace<br>Cape Town 8001</p>
    <p class="contact-email">hello@heroncollective.co.uk</p>
  </div>
</section>

</body>
</html>
```